Mandarin tuition, language and travel services

We need a website for a new startup company, which offers Mandarin tuition, translating and interpreting, and travel services. Our company is based in Jersey, a British channel island. We would like a creative and modern professional website. Preferably with some animations. The attached is a website, which style we would prefer:
http://www.quorvabelt.net/
We have also attached our logo for your reference
We would also like to see designs using black, red and orange, which corresponds with our logo colours. The cartoon images could be travel resorts in China, and the president of China waving to the web-browsers. Of course, we wouldn't wish to restrain the designers creativity. Any creative and interesting ideas are welcomed! We look forward to hearing from you!

Target Market(s)

school children and adults

Industry/Entity Type

It Company

Number of Pages Required

3 page

Requirements
Must have
• We would prefer a small 3 pages website, if possible. The 3 pages need to be Services, News Room, and Contact us.

```html
<!DOCTYPE html>
<html lang="en">
<head>
<meta charset="utf-8">
<title>Lantern Lingua</title>
<link href="https://fonts.googleapis.com/css2?family=Open+Sans:wght@400;600;700&family=Alfa+Slab+One&display=swap" rel="stylesheet">
<style>
  :root {
    --ink: #161616;
    --ink-soft: #1f1f1f;
    --red: #d21f26;
    --red-deep: #b5161c;
    --gold: #e0b43a;
    --white: #ffffff;
    --text-muted: #d6d6d6;
    --line: #5a5a5a;
  }
  * { margin: 0; padding: 0; box-sizing: border-box; }
  html, body { width: 841px; height: 1200px; overflow: hidden; }
  body {
    background: var(--ink);
    font-family: "Open Sans", sans-serif;
    color: var(--white);
    position: relative;
  }

  /* Header */
  .site-header {
    position: absolute; left: 0; top: 0; width: 841px; height: 127px;
    background: radial-gradient(ellipse at center, #232323 0%, var(--ink) 75%);
  }
  .header-icon {
    position: absolute; top: 31px; width: 36px; height: 36px; border-radius: 50%;
    background: var(--red); display: flex; align-items: center; justify-content: center;
  }
  .header-icon.phone { left: 52px; }
  .header-icon.mail { left: 752px; }
  .brand {
    position: absolute; left: 0; width: 841px; top: 30px; text-align: center;
    font-family: "Open Sans", sans-serif; font-weight: 700; font-size: 20px;
    color: var(--white); letter-spacing: 0.5px;
  }
  .brand .brand-dot {
    display: inline-block; width: 14px; height: 14px; border-radius: 50%;
    background: var(--red); margin-right: 7px; vertical-align: -1px;
  }
  .main-nav {
    position: absolute; left: 0; top: 94px; width: 841px;
    display: flex; justify-content: center; align-items: center; gap: 14px;
    font-weight: 700; font-size: 13px; letter-spacing: 0.2px;
  }
  .main-nav .sep {
    width: 6px; height: 6px; background: var(--gold); transform: rotate(45deg);
  }

  /* Hero */
  .hero {
    position: absolute; left: 0; top: 127px; width: 841px; height: 413px;
    background:
      linear-gradient(180deg, #f3efe0 0%, #e9dfb8 28%, #b49a32 44%, #8a8a32 52%, #c9a640 64%, #8c7a28 82%, #6f6a2a 100%);
  }
  .hero-arrow {
    position: absolute; top: 191px; width: 26px; height: 26px;
  }
  .hero-arrow.prev { left: 30px; }
  .hero-arrow.next { left: 784px; }

  /* Service tiles */
  .services {
    position: absolute; left: 0; top: 540px; width: 841px; height: 164px;
    display: flex;
  }
  .service-tile {
    position: relative; width: 280.33px; height: 164px;
    border-right: 1px solid #222;
  }
  .service-tile.tuition { background: linear-gradient(120deg, #e8edf2 0%, #c8d2dc 55%, #4a4e56 100%); }
  .service-tile.translating { background: linear-gradient(100deg, #e6e2dc 0%, #cfc8bf 55%, #2b2b2b 100%); }
  .service-tile.travel { background: linear-gradient(180deg, #c6d8ea 0%, #a9bfd2 45%, #5b6f4a 75%, #3f5232 100%); }
  .service-label {
    position: absolute; left: 6px; right: 6px; top: 112px; height: 46px;
    background: rgba(25,25,25,0.88);
    display: flex; align-items: center; justify-content: center; text-align: center;
    font-weight: 700; font-size: 16px; line-height: 17px; text-transform: uppercase;
  }

  /* Welcome */
  .welcome {
    position: absolute; left: 0; top: 704px; width: 841px; height: 386px;
    background: radial-gradient(ellipse at center, #202020 0%, var(--ink) 80%);
  }
  .welcome-frame { position: absolute; left: 0; top: 0; }
  .welcome-title {
    position: absolute; left: 0; width: 841px; top: 84px; text-align: center;
    font-family: "Alfa Slab One", serif; font-size: 26px; letter-spacing: 0.8px;
    color: var(--white);
  }
  .welcome-title .accent { color: var(--red); }
  .welcome-rule {
    position: absolute; left: 238px; top: 128px; width: 365px; height: 1px; background: var(--line);
  }
  .welcome-rule::after {
    content: ""; position: absolute; left: 176px; top: -3px; width: 7px; height: 7px;
    background: var(--gold); transform: rotate(45deg);
  }
  .welcome-copy {
    position: absolute; left: 95px; width: 651px; top: 157px;
    text-align: center; font-size: 11.2px; line-height: 16.8px; color: var(--text-muted);
  }

  /* Footer */
  .site-footer {
    position: absolute; left: 0; top: 1090px; width: 841px; height: 110px;
    background: var(--red);
  }
  .contact-item {
    position: absolute; top: 18px; display: flex; gap: 10px;
    font-size: 10.5px; line-height: 15px;
  }
  .contact-item svg { flex: none; }
  .contact-item.address { left: 51px; }
  .contact-item.phone { left: 198px; }
  .contact-item.email { left: 323px; }
  .social-links {
    position: absolute; left: 688px; top: 19px; display: flex; gap: 4px;
  }
  .social-links span {
    width: 22px; height: 22px; border-radius: 50%; border: 1.5px solid var(--white);
  }
  .footer-nav {
    position: absolute; left: 51px; top: 84px; display: flex; gap: 13px;
    font-size: 10.5px; text-transform: uppercase;
  }
  .copyright {
    position: absolute; right: 49px; top: 84px; font-size: 10.5px; text-transform: uppercase;
  }
</style>
</head>
<body>

<header class="site-header">
  <div class="header-icon phone">
    <svg width="16" height="16" viewBox="0 0 24 24" fill="none" stroke="#fff" stroke-width="1.8" stroke-linecap="round" stroke-linejoin="round"><path d="M22 16.9v3a2 2 0 0 1-2.2 2 19.8 19.8 0 0 1-8.6-3.1 19.5 19.5 0 0 1-6-6A19.8 19.8 0 0 1 2.1 4.2 2 2 0 0 1 4.1 2h3a2 2 0 0 1 2 1.7c.1.9.4 1.8.7 2.7a2 2 0 0 1-.5 2.1L8 9.8a16 16 0 0 0 6 6l1.3-1.3a2 2 0 0 1 2.1-.4c.9.3 1.8.6 2.7.7a2 2 0 0 1 1.7 2z"/></svg>
  </div>
  <div class="brand"><span class="brand-dot"></span>Lantern Lingua</div>
  <div class="header-icon mail">
    <svg width="18" height="14" viewBox="0 0 18 14" fill="none" stroke="#fff" stroke-width="1.4"><rect x="1" y="1" width="16" height="12" rx="1"/><path d="M1 1l8 7 8-7M1 13l6-6M17 13l-6-6"/></svg>
  </div>
  <nav class="main-nav">
    <span>HOME</span><i class="sep"></i>
    <span>ABOUT US</span><i class="sep"></i>
    <span>SERVICES</span><i class="sep"></i>
    <span>NEWS ROOM</span><i class="sep"></i>
    <span>CONTACT US</span>
  </nav>
</header>

<section class="hero" role="img" aria-label="Photo of a red Chinese pavilion among autumn trees reflected in a calm lake">
  <svg class="hero-arrow prev" viewBox="0 0 26 26"><circle cx="13" cy="13" r="12" fill="rgba(0,0,0,0.35)" stroke="#fff" stroke-width="1.5"/><path d="M15 8l-5 5 5 5" fill="none" stroke="#fff" stroke-width="1.8"/></svg>
  <svg class="hero-arrow next" viewBox="0 0 26 26"><circle cx="13" cy="13" r="12" fill="rgba(0,0,0,0.35)" stroke="#fff" stroke-width="1.5"/><path d="M11 8l5 5-5 5" fill="none" stroke="#fff" stroke-width="1.8"/></svg>
</section>

<section class="services">
  <div class="service-tile tuition" role="img" aria-label="Photo of a smiling woman writing Chinese characters on a whiteboard">
    <div class="service-label">Mandarin Tuition<br>Service</div>
  </div>
  <div class="service-tile translating" role="img" aria-label="Photo of two hands with pens over a document">
    <div class="service-label">Translating &amp;<br>Interpreting Service</div>
  </div>
  <div class="service-tile travel" role="img" aria-label="Photo of a Chinese temple tower on a wooded hillside">
    <div class="service-label">Travel<br>Service</div>
  </div>
</section>

<section class="welcome">
  <svg class="welcome-frame" width="841" height="386" viewBox="0 0 841 386" fill="none">
    <g stroke="#6a6a6a" stroke-width="1">
      <line x1="92" y1="44" x2="749" y2="44"/>
      <line x1="92" y1="48" x2="749" y2="48"/>
      <line x1="92" y1="332" x2="749" y2="332"/>
      <line x1="92" y1="336" x2="749" y2="336"/>
      <line x1="63" y1="62" x2="63" y2="316"/>
      <line x1="67" y1="62" x2="67" y2="316"/>
      <line x1="774" y1="62" x2="774" y2="316"/>
      <line x1="778" y1="62" x2="778" y2="316"/>
    </g>
    <g stroke="#e0b43a" stroke-width="1.5">
      <circle cx="65" cy="40" r="6"/><line x1="65" y1="46" x2="65" y2="62"/><line x1="71" y1="40" x2="88" y2="40"/>
      <circle cx="776" cy="40" r="6"/><line x1="776" y1="46" x2="776" y2="62"/><line x1="770" y1="40" x2="753" y2="40"/>
      <circle cx="65" cy="340" r="6"/><line x1="65" y1="334" x2="65" y2="318"/><line x1="71" y1="340" x2="88" y2="340"/>
      <circle cx="776" cy="340" r="6"/><line x1="776" y1="334" x2="776" y2="318"/><line x1="770" y1="340" x2="753" y2="340"/>
    </g>
  </svg>
  <h1 class="welcome-title">WELCOME TO <span class="accent">LANTERN LINGUA</span></h1>
  <div class="welcome-rule"></div>
  <p class="welcome-copy">Lorem ipsum dolor sit amet, consectetur adipiscing elit, sed do eiusmod tempor incididunt ut labore et dolore magna aliqua. Ut enim ad minim veniam, quis nostrud exercitation ullamco laboris nisi ut aliquip ex ea commodo consequat. Duis aute irure dolor in reprehenderit in voluptate velit esse cillum dolore eu fugiat nulla pariatur. Excepteur sint occaecat cupidatat non proident, sunt in culpa qui officia deserunt mollit anim id est laborum. Sed ut perspiciatis unde omnis iste natus error sit voluptatem accusantium doloremque laudantium, totam rem aperiam, eaque ipsa quae ab illo inventore veritatis et quasi architecto beatae vitae dicta sunt explicabo. Nemo enim ipsam voluptatem quia voluptas sit aspernatur aut odit aut fugit, sed quia consequuntur magni dolores eos qui ratione voluptatem sequi nesciunt. Neque porro quisquam est, qui dolorem ipsum quia dolor sit amet, consectetur, adipisci velit, sed quia non numquam eius modi tempora incidunt ut labore et dolore magnam aliquam quaerat voluptatem.</p>
</section>

<footer class="site-footer">
  <div class="contact-item address">
    <svg width="20" height="20" viewBox="0 0 20 20" fill="none" stroke="#fff" stroke-width="1.3"><circle cx="10" cy="10" r="9"/><path d="M10 15s-3.5-3.6-3.5-6a3.5 3.5 0 0 1 7 0c0 2.4-3.5 6-3.5 6z"/><circle cx="10" cy="9" r="1.2"/></svg>
    <div>Your Company LTD.<br>Street Name, 000000<br>City Name</div>
  </div>
  <div class="contact-item phone">
    <svg width="20" height="20" viewBox="0 0 20 20" fill="none" stroke="#fff" stroke-width="1.3"><circle cx="10" cy="10" r="9"/><path d="M7 5.5l1.5 2.2-1 1.2a6 6 0 0 0 3.6 3.6l1.2-1 2.2 1.5-.8 1.6c-3.6.4-7.9-3.9-7.5-7.5z"/></svg>
    <div>Phone<br>1-000-000-0000</div>
  </div>
  <div class="contact-item email">
    <svg width="20" height="20" viewBox="0 0 20 20" fill="none" stroke="#fff" stroke-width="1.3"><circle cx="10" cy="10" r="9"/><rect x="5.5" y="7" width="9" height="6.5"/><path d="M5.5 7l4.5 3.5L14.5 7"/></svg>
    <div>Email<br>info@lanternlingua.com</div>
  </div>
  <div class="social-links" aria-label="Social links">
    <span></span><span></span><span></span><span></span>
  </div>
  <nav class="footer-nav">
    <span>Home</span><span>About Us</span><span>Services</span><span>News Room</span><span>Contact Us</span>
  </nav>
  <div class="copyright">© 2016 Lantern Lingua. All Rights Reserved</div>
</footer>

</body>
</html>
```